Z-Reel Carnival Podcast Cover Design

We need a podcast cover (square design) for a podcast called Z-Reel Carnival.
MANDATORY: Z-REEL CARNIVAL
OPTIONAL: with The Creature Nerd Dale Furnow

Z-Reel Carnival is a movie podcast dedicated to covering all of the cult oddities you saw in theaters and video stores as a kid but never got to rent or watch. Focusing on obscure horror, cult oddities, action movies, exploitation movies, foreign knockoffs, and more, this a show designed to help you take a trip down memory lane or find new weird movies to add to your streaming queue. Come take a walk on the wild side of cinema at Z-Reel Carnival,..where one person's trash movie is our treasure.
##
Fonts that fit the vibe we're going for:
https://www.typevault.example/sets/grindhouse-drip-font-kelvorn-studio
https://www.pinboardly.example/pin/481926035517204963/
https://www.typevault.example/sets/grindhouse-vintage-font-kelvorn-studio

Target Market(s)

Primarily male, although we have some female fans as well. Podcast fans of B-movies (inexpensively made and a bit outrageous), cult movies, weird movies, old movies, horror movies, and action films.

Industry/Entity Type

Media - Movies -Podcast

Font styles to use
Other font styles liked:
• Fonts that fit the vibe: Fonts: https://www.typevault.example/sets/grindhouse-drip-font-kelvorn-studio https://www.pinboardly.example/pin/481926035517204963/ https://www.typevault.example/sets/grindhouse-vintage-font-kelvorn-studio

Colors
EB3D1F
EC4F4E
F09395
F8D3D4
FCEDEE

Requirements
Must have
• Z-REEL CARNIVAL
Nice to have
• 1) with The Creature Nerd Dale Furnow; 2) VISUALS: VHS tapes

```html
<!DOCTYPE html>
<html lang="en">
<head>
<meta charset="utf-8">
<title>Z-Reel Carnival — Podcast Cover</title>
<link rel="stylesheet" href="https://fonts.googleapis.com/css2?family=Creepster&family=Rubik+Dirt&display=swap">
<style>
  :root {
    --bg-deep: #13222a;
    --bg-main: #1b2c34;
    --title-white: #ffffff;
    --title-yellow: #f0c014;
    --strip-tone: #2e434c;
    --tape-dark: #3d3f41;
    --tape-mid: #545658;
  }
  * { margin: 0; padding: 0; box-sizing: border-box; }
  html, body { width: 1200px; height: 1200px; overflow: hidden; background: var(--bg-main); }
  .cover {
    position: relative;
    width: 1200px;
    height: 1200px;
    overflow: hidden;
    background: radial-gradient(ellipse at 60% 40%, var(--bg-main) 0%, var(--bg-deep) 100%);
  }
  .cover svg { position: absolute; inset: 0; display: block; }
  .title { font-family: "Creepster", fantasy; }
  .host { font-family: "Rubik Dirt", system-ui, sans-serif; }
</style>
</head>
<body>
<main class="cover">
  <svg width="1200" height="1200" viewBox="0 0 1200 1200">
    <!-- decorative film reel strip, soft band -->
    <path class="film-strip" role="img" aria-label="Faint curling strip of film running down the left side"
          d="M0 -20 L190 -20 C330 180 440 420 430 640 C420 800 330 880 150 940 L0 990 L0 870 C160 820 270 760 280 620 C295 420 200 200 60 60 L0 0 Z"
          fill="var(--strip-tone)" opacity="0.45"/>

    <!-- title -->
    <text class="title" x="82" y="362" textLength="845" lengthAdjust="spacingAndGlyphs"
          font-size="250" fill="var(--title-white)">Z-REEL</text>
    <text class="title" x="265" y="630" textLength="850" lengthAdjust="spacingAndGlyphs"
          font-size="250" fill="var(--title-yellow)">CARNIVAL</text>

    <!-- host credit -->
    <text class="host" x="121" y="924" textLength="82" lengthAdjust="spacingAndGlyphs"
          font-size="40" fill="var(--title-white)">WITH</text>
    <text class="host" x="124" y="1000" textLength="565" lengthAdjust="spacingAndGlyphs"
          font-size="80" fill="var(--title-yellow)">THE CREATURE NERD</text>
    <text class="host" x="127" y="1098" textLength="560" lengthAdjust="spacingAndGlyphs"
          font-size="100" fill="var(--title-white)">DALE FURNOW</text>

    <!-- VHS stack area -->
    <rect class="vhs-stack" role="img" aria-label="Stack of VHS video cassettes, the top tape showing a white and yellow label"
          x="750" y="646" width="450" height="520" rx="6"
          fill="url(#tapeTone)"/>
    <defs>
      <linearGradient id="tapeTone" x1="0" y1="0" x2="0" y2="1">
        <stop offset="0" stop-color="var(--tape-dark)"/>
        <stop offset="1" stop-color="var(--tape-mid)"/>
      </linearGradient>
    </defs>
  </svg>
</main>
</body>
</html>
```